Derek Milbourne needs a single album cover

I need an single album cover for a song I wrote called "Still Harbor". I would like the design to Illustrate how gods grace covers all sin.

Requirements
Must have
• The song title "Still Harbor" And my name Derek Milbourne

```html
<!DOCTYPE html>
<html lang="en">
<head>
<meta charset="utf-8">
<title>Still Harbor — Derek Milbourne</title>
<link rel="stylesheet" href="https://fonts.googleapis.com/css2?family=Quicksand:wght@500;600&display=swap">
<style>
  :root {
    --page-bg: #2a2623;
    --cover-deep: #1c1420;
    --cover-plum: #4a2a44;
    --cover-rose: #8a4d6a;
    --glow-warm: #ffd9b8;
    --accent-green: #7bd66a;
    --accent-violet: #9a5cc8;
    --type-light: #ffffff;
  }
  * { margin: 0; padding: 0; box-sizing: border-box; }
  html, body {
    width: 1200px;
    height: 902px;
    overflow: hidden;
    background: var(--page-bg);
  }
  .album-cover {
    position: absolute;
    left: 250px;
    top: 101px;
    width: 700px;
    height: 700px;
    overflow: hidden;
    background:
      radial-gradient(circle at 30% 20%, var(--cover-rose) 0%, transparent 55%),
      radial-gradient(circle at 80% 30%, var(--cover-plum) 0%, transparent 60%),
      linear-gradient(180deg, var(--cover-plum) 0%, var(--cover-deep) 75%);
    font-family: "Quicksand", sans-serif;
    color: var(--type-light);
  }
  .artist-photo {
    position: absolute;
    left: 500px;
    top: 110px;
    width: 200px;
    height: 500px;
    background: linear-gradient(180deg, rgba(120,80,90,0.55) 0%, rgba(40,30,45,0.75) 60%, rgba(25,20,30,0.5) 100%);
    border-radius: 80px 20px 10px 40px;
  }
  .cover-lines {
    position: absolute;
    inset: 0;
  }
  .light-flare {
    position: absolute;
    left: 180px;
    top: 380px;
    width: 220px;
    height: 150px;
    background: radial-gradient(ellipse at center, rgba(255,240,220,0.95) 0%, rgba(255,190,150,0.45) 22%, transparent 65%);
  }
  .title-lead {
    position: absolute;
    left: 50px;
    top: 268px;
    font-size: 38px;
    font-weight: 600;
    letter-spacing: 1px;
    line-height: 1;
  }
  .title-main {
    position: absolute;
    left: 44px;
    top: 312px;
    font-size: 142px;
    font-weight: 500;
    line-height: 1;
    letter-spacing: -2px;
  }
  .artist-name {
    position: absolute;
    right: 42px;
    top: 460px;
    font-size: 28px;
    font-weight: 500;
    line-height: 1;
  }
</style>
</head>
<body>
  <main class="album-cover">
    <div class="artist-photo" role="img" aria-label="Portrait of the artist kneeling, chin resting on folded hands, looking upward"></div>
    <svg class="cover-lines" width="700" height="700" viewBox="0 0 700 700" aria-hidden="true">
      <line x1="0" y1="453" x2="700" y2="448" stroke="var(--accent-green)" stroke-width="1.5" opacity="0.7"/>
      <line x1="0" y1="458" x2="700" y2="454" stroke="var(--accent-violet)" stroke-width="1" opacity="0.6"/>
      <line x1="60" y1="700" x2="520" y2="380" stroke="var(--accent-violet)" stroke-width="1" opacity="0.35"/>
      <line x1="150" y1="700" x2="600" y2="420" stroke="var(--accent-violet)" stroke-width="1" opacity="0.25"/>
    </svg>
    <div class="light-flare"></div>
    <p class="title-lead">STILL</p>
    <h1 class="title-main">HARBOR</h1>
    <p class="artist-name">DEREK MILBOURNE</p>
  </main>
</body>
</html>
```